Visiting Card / Envelope design / Letterhead for MARLOW

I need for our company a new

Visiting Card / Envelope design / Letterhead

please see enclosed logo:

Use any US address and the company's name is MARLOW GENERAL CONSTRUCTION INC.

BE CREATIVE, not usual ))

```html
<!DOCTYPE html>
<html lang="en">
<head>
<meta charset="utf-8">
<title>Marlow General Construction – Stationery</title>
<link href="https://fonts.googleapis.com/css2?family=Open+Sans:wght@400;600;700&family=Quicksand:wght@400;500&display=swap" rel="stylesheet">
<style>
  :root {
    --bg: #3a3a3a;
    --paper: #ffffff;
    --card-paper: #f7f5f6;
    --red: #b8173d;
    --red-soft: #d9687a;
    --purple: #3c2f86;
    --purple-soft: #7b70b0;
    --gray-band: #b5b5b5;
    --gray-dark: #9c9c9c;
  }
  * { margin: 0; padding: 0; box-sizing: border-box; }
  html, body { width: 802px; height: 1200px; overflow: hidden; background: var(--bg); }
  body { position: relative; font-family: "Open Sans", sans-serif; }

  /* Visiting card */
  .visiting-card {
    position: absolute; left: 78px; top: 49px; width: 662px; height: 395px;
    background: var(--card-paper);
    border: 3px solid var(--red);
    box-shadow: inset 0 0 0 3px var(--purple);
    overflow: hidden;
  }
  .visiting-card .stripes { position: absolute; left: 0; top: 0; width: 662px; height: 395px; }
  .brand-mark {
    position: absolute; left: 0; right: 0; top: 120px; text-align: center;
    font-family: "Open Sans", sans-serif; font-weight: 600; font-size: 58px;
    color: var(--purple); letter-spacing: 1px; line-height: 1;
  }
  .company-title {
    position: absolute; left: 0; right: 0; top: 214px; text-align: center;
    font-weight: 600; font-size: 19px; color: var(--red); letter-spacing: 0.2px;
  }
  .contact-block {
    position: absolute; left: 316px; top: 270px;
    font-family: "Quicksand", sans-serif; font-size: 20px; line-height: 20px;
    color: var(--red);
  }
  .card-email {
    position: absolute; left: 316px; top: 362px;
    font-family: "Quicksand", sans-serif; font-size: 15px; color: var(--red);
  }

  /* Letterhead */
  .letterhead {
    position: absolute; left: 64px; top: 580px; width: 380px; height: 492px;
    background: var(--paper);
    border-top: 3px solid var(--purple); border-right: 2px solid var(--purple);
    overflow: hidden;
  }
  .letterhead svg { position: absolute; left: 0; top: 0; }
  .letterhead .brand-small {
    position: absolute; left: 24px; top: 28px;
    font-weight: 600; font-size: 24px; color: var(--purple);
  }

  /* Envelope */
  .envelope {
    position: absolute; left: 470px; top: 720px; width: 290px; height: 160px;
    background: var(--paper); overflow: hidden;
  }
  .envelope svg { position: absolute; left: 0; top: 0; }
  .envelope .brand-small {
    position: absolute; right: 22px; top: 52px;
    font-weight: 600; font-size: 26px; color: var(--purple);
  }
  .envelope-email {
    position: absolute; left: 14px; bottom: 6px;
    font-family: "Quicksand", sans-serif; font-size: 13px; color: #ffffff; letter-spacing: 0.5px;
  }
</style>
</head>
<body>

  <section class="visiting-card">
    <svg class="stripes" width="662" height="395" viewBox="0 0 662 395" aria-hidden="true">
      <defs>
        <linearGradient id="redStripe" x1="0" y1="0" x2="1" y2="0.6">
          <stop offset="0" stop-color="#d9687a"/>
          <stop offset="1" stop-color="#f3d3d8" stop-opacity="0.3"/>
        </linearGradient>
        <linearGradient id="purpleStripe" x1="0" y1="0" x2="1" y2="0.6">
          <stop offset="0" stop-color="#ffffff" stop-opacity="0.4"/>
          <stop offset="1" stop-color="#6a5fa6"/>
        </linearGradient>
      </defs>
      <polygon points="3,198 215,392 126,392 3,278" fill="url(#redStripe)"/>
      <polygon points="91,258 175,258 296,392 215,392" fill="url(#purpleStripe)"/>
    </svg>
    <div class="brand-mark">MARLOW</div>
    <div class="company-title">MARLOW GENERAL CONSTRUCTION INC.</div>
    <div class="contact-block">
      MARLOWConstructors, Inc.<br>
      P.O. Box 480317<br>
      Franklin, TN 37064<br>
      (615) 555-0148
    </div>
    <div class="card-email">mail@marlowconstructor.com</div>
  </section>

  <section class="letterhead">
    <svg width="380" height="492" viewBox="0 0 380 492" aria-hidden="true">
      <path d="M0,130 C10,300 80,440 230,470 L0,470 Z" fill="var(--red)"/>
      <rect x="0" y="470" width="380" height="22" fill="var(--gray-band)"/>
    </svg>
    <div class="brand-small">MARLOW</div>
  </section>

  <section class="envelope">
    <svg width="290" height="160" viewBox="0 0 290 160" aria-hidden="true">
      <path d="M0,0 L160,0 C80,20 20,70 0,135 Z" fill="var(--red)"/>
      <rect x="0" y="135" width="290" height="25" fill="var(--gray-dark)"/>
    </svg>
    <div class="brand-small">MARLOW</div>
    <div class="envelope-email">mail@marlowconstructor.com</div>
  </section>

</body>
</html>
```